Update Dulmar & Co Powerpoint to Quillmere Partnership

Hi, about 2 years ago I had a great Powerpoint template produced for my business called Dulmar & Co. We have now changed the company name and logo to Quillmere Partnership and I would like you to update the presentation template pages to the new logo and design.

I attach:

1) The original Powerpoint presentation that was produced for Dulmar
2) The new Quillmere Partnership logo files
3) The initial Powerpoint presentation format that my UK designer has done to give you an idea of their approach
4) The Font files (Red Hat Display - medium)

It would be great to receive the new PP template by Tuesday 22nd July.

Please message me if you have any questions.
Thanks
Ned

```html
<!DOCTYPE html>
<html lang="en">
<head>
<meta charset="utf-8">
<title>Quillmere Partnership – Presentation Template</title>
<link href="https://fonts.googleapis.com/css2?family=Red+Hat+Display:ital,wght@0,400;0,500;0,700;0,900;1,400&display=swap" rel="stylesheet">
<style>
:root{
  --backdrop:#87999c;
  --teal:#0f3139;
  --teal-mid:#4b6a6f;
  --slate:#3e545a;
  --orange:#e1531b;
  --salmon:#e48c72;
  --ink:#333b3e;
  --muted:#9aa2a5;
  --rule:#d9dcdd;
  --paper:#ffffff;
  --row:#f1f2f2;
}
*{margin:0;padding:0;box-sizing:border-box}
html,body{width:1200px;height:1200px;overflow:hidden;background:var(--backdrop)}
body{font-family:"Red Hat Display",Arial,sans-serif;color:var(--ink)}
.stage{position:absolute;left:0;top:0;width:1932px;height:1932px;transform:scale(0.62112);transform-origin:0 0}
.slide{position:absolute;width:620px;height:348px;background:var(--paper);overflow:hidden}
.art{position:absolute;left:0;top:0;width:620px;height:348px}
.t{position:absolute;white-space:nowrap}
.tag{font-size:9px;line-height:1.15;color:var(--ink)}
.tag b{font-weight:700}
.tag.light{color:#fff}
.bar{position:absolute;width:30px;height:5px;background:var(--slate)}
.bar.white{background:#fff}
.heading{font-size:19px;line-height:1.35;color:var(--ink);font-weight:400}
.heading b{font-weight:700}
.sub{font-size:8px;letter-spacing:2.4px;font-style:italic;color:var(--muted)}
.body{font-size:6.6px;line-height:1.9;color:var(--ink);white-space:normal;text-align:justify}
.web{font-size:6px;letter-spacing:2.6px;color:var(--ink)}
.web.vert{writing-mode:vertical-rl;transform:rotate(180deg)}
.brand{position:absolute;display:flex;align-items:center;gap:5px;font-size:13px;font-weight:700;color:var(--teal);white-space:nowrap}
.brand .dot{width:11px;height:11px;border-radius:50%;background:var(--orange)}
.brand.big{font-size:34px;gap:12px;color:#fff}
.brand.big .dot{width:30px;height:30px}
.toc-num{position:absolute;width:22px;height:22px;border-radius:50%;color:#fff;font-size:8px;display:flex;align-items:center;justify-content:center;background:var(--teal)}
.toc-num.hot{background:var(--orange)}
.toc-mins{font-size:7px;font-style:italic}
.toc-title{font-size:10px}
.toc-desc{font-size:6.6px;line-height:1.8}
.toc-rule{position:absolute;height:1px;background:var(--rule);width:115px}
.vert-title{position:absolute;left:418px;top:65px;writing-mode:vertical-rl;transform:rotate(180deg);font-size:26px;color:var(--ink);white-space:nowrap}
.vert-title b{font-weight:700}
.mission{font-size:6.5px;font-weight:700;display:flex;align-items:center;gap:6px}
.price-table{position:absolute;left:90px;top:83px;width:438px;border-collapse:collapse;table-layout:fixed}
.price-table th{height:26px;color:#fff;font-size:14px;font-weight:700;text-align:left;padding-left:17px;background:var(--slate)}
.price-table th.hot{background:var(--orange)}
.price-table td{height:29.5px;font-size:5.5px;color:#8a9194;text-align:center;border-bottom:2px solid #fff}
.price-table tr:nth-child(odd) td{background:var(--row)}
.price-table tr:nth-child(even) td{background:#fff}
.price-table td .dash{display:inline-block;width:18px;height:1px;background:#aaa;vertical-align:middle}
.price-table tr.total td{height:55px;font-size:15px;font-weight:700;color:var(--ink);background:var(--row)}
.price-table tr.total td.hot{color:var(--orange)}
.section-title{font-size:17px;letter-spacing:.5px;color:var(--ink);text-align:center}
.section-title b{font-weight:700}
.item-icon{position:absolute;width:30px;height:30px;border-radius:50%;border:2px solid var(--slate)}
.item-icon.hot{border-color:var(--orange)}
.item-title{font-size:14px;font-weight:700;color:var(--slate)}
.item-title.hot{color:var(--orange)}
.item-text{font-size:5.5px;line-height:1.7;color:#8a9194}
.step{position:absolute;width:22px;height:22px;border-radius:50%;background:var(--slate);color:#fff;font-size:9px;font-weight:700;display:flex;align-items:center;justify-content:center}
.step.hot{background:var(--orange)}
.step-title{font-size:6.5px;font-weight:700;text-align:center;width:70px}
.step-text{font-size:5px;line-height:1.8;text-align:center;width:70px;color:#9aa2a5;white-space:normal}
.break-word{font-weight:900;color:#fff;letter-spacing:1px}
</style>
</head>
<body>
<div class="stage">

<!-- Row 1 -->
<section class="slide cover" style="left:26px;top:86px;background:var(--teal)">
  <svg class="art"><polygon points="0,0 390,0 228,348 0,348" fill="var(--salmon)" role="img" aria-label="Team working at a table with laptops, salmon tinted photo"/></svg>
  <div class="t tag light" style="left:32px;top:28px"><b>Quillmere</b><br>Partnership</div>
  <div class="bar white" style="left:80px;top:158px"></div>
  <div class="t" style="left:80px;top:170px;color:#fff;font-size:24px;line-height:1.05">Presentation<br><b>Title</b></div>
  <div class="t" style="left:80px;top:228px;color:#fff;font-size:9px;letter-spacing:2px;font-style:italic">Monday 9th June, 2025</div>
  <div class="brand big" style="left:372px;top:152px"><span class="dot"></span>Quillmere</div>
  <div class="t web" style="left:500px;top:313px;color:#fff">www.company.com</div>
</section>

<section class="slide cover-alt" style="left:656px;top:86px;background:#8b8d8e">
  <svg class="art">
    <rect width="620" height="348" fill="#9a9c9d" role="img" aria-label="Overhead black and white photo of coffee cups and laptops on a desk"/>
    <polygon points="0,0 390,0 210,348 0,348" fill="var(--teal)" opacity=".82"/>
    <polygon points="0,0 120,0 0,230" fill="var(--orange)"/>
  </svg>
  <div class="t tag light" style="left:32px;top:28px"><b>Quillmere</b><br>Partnership</div>
  <div class="bar white" style="left:62px;top:160px"></div>
  <div class="t" style="left:61px;top:172px;color:#fff;font-size:24px;line-height:1.08">Presentation Title<br><b>Goes Here</b></div>
  <div class="t" style="left:61px;top:231px;color:#fff;font-size:8px;letter-spacing:2.2px;font-style:italic">Subtitle of Presentation</div>
</section>

<section class="slide intro" style="left:1286px;top:86px">
  <svg class="art">
    <polygon points="445,0 620,0 620,40 475,348 320,348" fill="var(--teal)"/>
    <path d="M335,30 Q420,0 500,40 L530,348 L300,348 Z" fill="url(#skin)" role="img" aria-label="Smiling businesswoman holding a tablet"/>
    <defs><linearGradient id="skin" x1="0" y1="0" x2="0" y2="1"><stop offset="0" stop-color="#b9a89c"/><stop offset="1" stop-color="#e4e0dc"/></linearGradient></defs>
    <polygon points="585,172 596,172 526,300 515,300" fill="var(--orange)"/>
    <polygon points="566,222 574,222 531,300 523,300" fill="var(--teal)"/>
  </svg>
  <div class="t tag" style="left:32px;top:28px"><b>Quillmere</b><br>Partnership</div>
  <div class="bar" style="left:78px;top:95px"></div>
  <div class="t" style="left:78px;top:112px;font-size:19px">Introduction</div>
  <div class="t sub" style="left:78px;top:145px;color:var(--salmon)">Lorem ipsum dolor sit</div>
  <div class="t body" style="left:78px;top:168px;width:178px">Lorem Ipsum is simply dummy text of the printing and typesetting industry. Lorem Ipsum has been the industry's standard dummy text ever since the 1500s, when an unknown printer took a</div>
  <div class="t" style="left:78px;top:292px;font-size:8px;font-style:italic">Lorem ipsum</div>
  <div class="brand" style="left:138px;top:283px;font-size:20px;gap:7px"><span class="dot" style="width:15px;height:15px"></span>Quillmere</div>
  <div class="t web vert" style="left:592px;top:240px">www.company.com</div>
</section>

<!-- Row 2 -->
<section class="slide toc" style="left:26px;top:443px">
  <svg class="art">
    <line x1="137" y1="25" x2="450" y2="25" stroke="var(--ink)" stroke-width="2"/>
    <rect x="495" y="0" width="93" height="348" fill="#a3a5a6" role="img" aria-label="Black and white desk photo strip"/>
  </svg>
  <div class="t tag" style="left:30px;top:20px"><b>Quillmere</b><br>Partnership</div>

  <div class="toc-num" style="left:55px;top:67px">01</div>
  <div class="t toc-mins" style="left:92px;top:47px">15 mins.</div>
  <div class="t toc-title" style="left:92px;top:65px">Title Goes Here</div>
  <div class="t toc-desc" style="left:92px;top:81px">Li Europan lingues es<br>membres del sam familie.</div>
  <div class="toc-rule" style="left:70px;top:127px"></div>
  <div class="toc-num hot" style="left:55px;top:154px">02</div>
  <div class="t toc-mins" style="left:92px;top:139px">15 mins.</div>
  <div class="t toc-title" style="left:92px;top:157px">Title Goes Here</div>
  <div class="t toc-desc" style="left:92px;top:173px">Li Europan lingues es<br>membres del sam familie.</div>
  <div class="toc-rule" style="left:70px;top:214px"></div>
  <div class="toc-num" style="left:55px;top:241px">03</div>
  <div class="t toc-mins" style="left:92px;top:226px">15 mins.</div>
  <div class="t toc-title" style="left:92px;top:245px">Title Goes Here</div>
  <div class="t toc-desc" style="left:92px;top:261px">Li Europan lingues es<br>membres del sam familie.</div>

  <div class="toc-num" style="left:220px;top:67px">04</div>
  <div class="t toc-mins" style="left:261px;top:47px">15 mins.</div>
  <div class="t toc-title" style="left:261px;top:65px">Title Goes Here</div>
  <div class="t toc-desc" style="left:261px;top:81px">Li Europan lingues es<br>membres del sam familie.</div>
  <div class="toc-rule" style="left:260px;top:127px"></div>
  <div class="toc-num hot" style="left:220px;top:154px">05</div>
  <div class="t toc-mins" style="left:261px;top:139px">15 mins.</div>
  <div class="t toc-title" style="left:261px;top:157px">Title Goes Here</div>
  <div class="t toc-desc" style="left:261px;top:173px">Li Europan lingues es<br>membres del sam familie.</div>
  <div class="toc-rule" style="left:260px;top:214px"></div>
  <div class="toc-num" style="left:220px;top:241px">06</div>
  <div class="t toc-mins" style="left:261px;top:226px">15 mins.</div>
  <div class="t toc-title" style="left:261px;top:245px">Title Goes Here</div>
  <div class="t toc-desc" style="left:261px;top:261px">Li Europan lingues es<br>membres del sam familie.</div>

  <div class="vert-title">Table of <b>Contents</b></div>
  <div class="brand" style="left:372px;top:311px"><span class="dot"></span>Quillmere</div>
  <div class="t" style="left:601px;top:328px;font-size:6px">4</div>
</section>

<section class="slide title-city" style="left:656px;top:443px">
  <svg class="art">
    <defs><linearGradient id="city" x1="0" y1="0" x2="1" y2="0"><stop offset="0" stop-color="#f2f3f3"/><stop offset=".45" stop-color="#c9cccd"/><stop offset="1" stop-color="#3a3f41"/></linearGradient></defs>
    <rect width="572" height="348" fill="url(#city)" role="img" aria-label="Looking up at glass skyscrapers, black and white"/>
    <polygon points="180,348 380,0 572,0 572,348" fill="#2c3133" opacity=".55"/>
    <polygon points="236,190 245,190 205,262 196,262" fill="var(--teal)"/>
    <polygon points="230,232 240,232 205,296 195,296" fill="var(--orange)"/>
  </svg>
  <div class="t tag" style="left:32px;top:28px"><b>Quillmere</b><br>Partnership</div>
  <div class="bar" style="left:60px;top:66px"></div>
  <div class="t" style="left:59px;top:82px;font-size:19px;line-height:1.36">PRESENTATION<br>TITLE <b>GOES</b><br><b>HERE</b></div>
  <div class="t sub" style="left:128px;top:136px">Presentation Goes Here</div>
  <div class="t body" style="left:62px;top:191px;width:103px">Lorem Ipsum is simply dummy text of the printing and typesetting industry. Lorem Ipsum has been the</div>
  <div class="t web" style="left:32px;top:313px">www.company.com</div>
</section>

<section class="slide split-photo" style="left:1286px;top:443px">
  <svg class="art">
    <polygon points="0,0 190,0 270,120 0,120" fill="#8b6b55" role="img" aria-label="Overhead photo of a team meeting around a wooden table"/>
    <polygon points="0,128 275,128 360,348 0,348" fill="#7d604c" role="img" aria-label="Overhead photo of colleagues shaking hands over laptops"/>
    <polygon points="205,45 214,45 288,170 279,170" fill="var(--teal)"/>
    <polygon points="243,92 252,92 290,170 281,170" fill="var(--orange)"/>
  </svg>
  <div class="bar" style="left:357px;top:93px"></div>
  <div class="t heading" style="left:357px;top:105px">Heading<br><b>Goes Here</b></div>
  <div class="t sub" style="left:357px;top:161px">Subtitle Goes Here</div>
  <div class="t body" style="left:357px;top:182px;width:178px">Lorem Ipsum is simply dummy text of the printing and typesetting industry. Lorem Ipsum has been the industry's standard dummy text ever since the 1500s, when an unknown printer took a</div>
  <div class="t web vert" style="left:592px;top:65px">www.company.com</div>
  <div class="brand" style="left:507px;top:304px"><span class="dot"></span>Quillmere</div>
</section>

<!-- Row 3 -->
<section class="slide two-column" style="left:26px;top:800px">
  <svg class="art">
    <rect x="78" y="0" width="187" height="220" fill="#dfe4ea" role="img" aria-label="Hand with a pen over printed bar charts"/>
    <rect x="122" y="228" width="142" height="120" fill="#7d6a5a" role="img" aria-label="Overhead photo of a team working at laptops"/>
    <rect x="104" y="245" width="7" height="68" fill="var(--orange)"/>
    <rect x="110" y="228" width="6" height="88" fill="var(--teal)"/>
  </svg>
  <div class="bar" style="left:303px;top:25px;background:#1f5fbf"></div>
  <div class="t heading" style="left:303px;top:37px">Heading<br><b>Goes Here</b></div>
  <div class="t sub" style="left:303px;top:94px">Subtitle Goes Here</div>
  <div class="t" style="left:303px;top:140px;font-size:13px;line-height:1.05"><b>Heading</b><br>Goes Here</div>
  <div class="t body" style="left:303px;top:182px;width:118px">Lorem Ipsum is simply dummy text of the printing and typesetting industry. Lorem Ipsum has been the industry's standard dummy text ever since the 1500s, when an unknown printer took a</div>
  <div class="t" style="left:454px;top:140px;font-size:13px;line-height:1.05"><b>Heading</b><br>Goes Here</div>
  <div class="t body" style="left:454px;top:182px;width:118px">Lorem Ipsum is simply dummy text of the printing and typesetting industry. Lorem Ipsum has been the industry's standard dummy text ever since the 1500s, when an unknown printer took a</div>
  <div class="t web vert" style="left:592px;top:65px">www.company.com</div>
  <div class="brand" style="left:507px;top:304px"><span class="dot"></span>Quillmere</div>
</section>

<section class="slide banner-photo" style="left:656px;top:800px">
  <svg class="art">
    <polygon points="0,175 490,175 440,315 0,315" fill="#c9c2b8" role="img" aria-label="Hands reviewing printed documents at a desk"/>
    <polygon points="440,195 448,195 500,280 492,280" fill="var(--teal)"/>
    <polygon points="455,215 464,215 496,280 487,280" fill="var(--orange)"/>
  </svg>
  <div class="t tag" style="left:32px;top:26px"><b>Quillmere</b> Partnership</div>
  <div class="bar" style="left:125px;top:64px"></div>
  <div class="t heading" style="left:125px;top:76px">Heading<br><b>Goes Here</b></div>
  <div class="t sub" style="left:125px;top:133px">Subtitle Goes Here</div>
  <div class="t body" style="left:311px;top:80px;width:182px">Lorem Ipsum is simply dummy text of the printing and typesetting industry. Lorem Ipsum has been the industry's standard dummy text ever since the 1500s, when an unknown printer took a</div>
  <div class="t web vert" style="left:592px;top:65px">www.company.com</div>
  <div class="brand" style="left:507px;top:304px"><span class="dot"></span>Quillmere</div>
</section>

<section class="slide missions" style="left:1286px;top:800px">
  <svg class="art">
    <polygon points="0,0 110,0 205,172 0,172" fill="#b4b9bc" role="img" aria-label="Skyscraper facades seen from below"/>
    <polygon points="40,185 190,185 265,308 110,308" fill="#8d9497" role="img" aria-label="Tall glass office tower"/>
    <polygon points="162,95 171,95 240,220 231,220" fill="var(--teal)"/>
    <polygon points="185,150 194,150 240,230 231,230" fill="var(--orange)"/>
  </svg>
  <div class="t tag" style="left:483px;top:26px"><b>Quillmere</b> Partnership</div>
  <div class="bar" style="left:260px;top:86px"></div>
  <div class="t heading" style="left:260px;top:98px">Heading<br><b>Goes Here</b></div>
  <div class="t sub" style="left:260px;top:155px">Subtitle Goes Here</div>
  <div class="t mission" style="left:478px;top:85px"><svg width="12" height="10"><path d="M1,5 L4,8 L11,1" stroke="var(--slate)" stroke-width="1.5" fill="none"/></svg>Mission 01</div>
  <div class="t mission" style="left:478px;top:112px"><svg width="12" height="10"><path d="M1,5 L4,8 L11,1" stroke="var(--slate)" stroke-width="1.5" fill="none"/></svg>Mission 02</div>
  <div class="t mission" style="left:478px;top:137px"><svg width="12" height="10"><path d="M1,5 L4,8 L11,1" stroke="#2a9fd6" stroke-width="1.5" fill="none"/></svg>Mission 03</div>
  <div class="t mission" style="left:478px;top:164px"><svg width="12" height="10"><path d="M1,5 L4,8 L11,1" stroke="var(--slate)" stroke-width="1.5" fill="none"/></svg>Mission 04</div>
  <div class="t body" style="left:311px;top:219px;width:180px">Lorem Ipsum is simply dummy text of the printing and typesetting industry. Lorem Ipsum has been the industry's standard dummy text ever since the 1500s, when an unknown printer took a</div>
  <div class="t web vert" style="left:592px;top:65px">www.company.com</div>
  <div class="brand" style="left:507px;top:304px"><span class="dot"></span>Quillmere</div>
</section>

<!-- Row 4 -->
<section class="slide chart-photo" style="left:26px;top:1157px">
  <svg class="art">
    <polygon points="292,275 432,0 620,0 620,265" fill="#e3e7ed" role="img" aria-label="Hand with a pen over printed charts"/>
    <polygon points="346,160 355,160 300,278 291,278" fill="var(--teal)"/>
    <polygon points="352,198 362,198 318,278 308,278" fill="var(--orange)"/>
  </svg>
  <div class="t tag" style="left:32px;top:26px"><b>Quillmere</b> Partnership</div>
  <div class="bar" style="left:80px;top:95px"></div>
  <div class="t heading" style="left:80px;top:107px">Heading<br><b>Goes Here</b></div>
  <div class="t sub" style="left:80px;top:164px">Subtitle Goes Here</div>
  <div class="t body" style="left:80px;top:196px;width:178px">Lorem Ipsum is simply dummy text of the printing and typesetting industry. Lorem Ipsum has been the industry's standard dummy text ever since the 1500s, when an unknown printer took a</div>
  <div class="t web" style="left:32px;top:313px">www.company.com</div>
  <div class="brand" style="left:507px;top:304px"><span class="dot"></span>Quillmere</div>
</section>

<section class="slide text-heavy" style="left:656px;top:1157px">
  <svg class="art">
    <polygon points="0,0 165,0 340,348 0,348" fill="#8f9293" role="img" aria-label="Black and white overhead desk scene with coffee and laptops"/>
    <polygon points="248,228 257,228 320,330 311,330" fill="var(--teal)"/>
    <polygon points="283,245 292,245 327,315 318,315" fill="var(--orange)"/>
  </svg>
  <div class="t tag" style="left:483px;top:26px"><b>Quillmere</b> Partnership</div>
  <div class="bar" style="left:262px;top:35px"></div>
  <div class="t heading" style="left:262px;top:47px">Heading<br><b>Goes Here</b></div>
  <div class="t sub" style="left:262px;top:104px">Subtitle Goes Here</div>
  <div class="t body" style="left:350px;top:127px;width:190px">Lorem Ipsum is simply dummy text of the printing and typesetting industry. Lorem Ipsum has been the industry's standard dummy text ever since the 1500s, when an unknown printer took a Lorem Ipsum is simply dummy text of the printing and typesetting industry. Lorem Ipsum has been the industry's standard dummy text ever since the 1500s, when an unknown printer took a</div>
  <div class="t body" style="left:405px;top:273px;width:130px;text-align:left">Lorem Ipsum is simply dummy text of the printing and typesetting industry. Lorem Ipsum has been the</div>
  <div class="t web vert" style="left:592px;top:65px">www.company.com</div>
  <div class="brand" style="left:507px;top:304px"><span class="dot"></span>Quillmere</div>
</section>

<section class="slide break" style="left:1286px;top:1157px;background:var(--teal)">
  <svg class="art">
    <polygon points="285,110 455,110 355,348 185,348" fill="var(--teal-mid)" opacity=".9"/>
    <polygon points="470,168 520,168 445,348 395,348" fill="var(--teal-mid)" opacity=".9"/>
    <polygon points="165,0 173,0 103,130 95,130" fill="var(--orange)"/>
    <polygon points="150,50 160,50 117,128 107,128" fill="var(--teal-mid)"/>
  </svg>
  <div class="t tag light" style="left:32px;top:26px"><b>Quillmere</b> Partnership</div>
  <div class="t" style="left:452px;top:36px;color:#fff;font-size:16px;font-weight:700;line-height:1.6">30<br>Minutes</div>
  <div class="t" style="left:452px;top:86px;color:#fff;font-size:6.5px;line-height:1.9">Lorem Ipsum is<br>simply dum</div>
  <div class="t break-word" style="left:75px;top:118px;font-size:66px">BREAK</div>
  <div class="t break-word" style="left:263px;top:208px;font-size:45px">SECTION</div>
  <div class="brand" style="left:100px;top:262px;color:#fff;font-size:14px"><span class="dot"></span>Quillmere</div>
  <div class="t web vert" style="left:592px;top:65px;color:#fff">www.company.com</div>
</section>

<!-- Row 5 -->
<section class="slide pricing" style="left:26px;top:1514px">
  <div class="t tag" style="left:32px;top:26px"><b>Quillmere</b> Partnership</div>
  <div class="bar" style="left:295px;top:36px"></div>
  <div class="t section-title" style="left:0;width:620px;top:48px">PRICING <b>TABLES</b></div>
  <table class="price-table">
    <tr><th>REGULAR</th><th class="hot">REGULAR 2</th><th>MEDIUM</th><th class="hot">MEDIUM 2</th></tr>
    <tr><td>Lorem Ipsum Dolor Sit</td><td>Lorem Ipsum Dolor Sit</td><td>Lorem Ipsum Dolor Sit</td><td>Lorem Ipsum Dolor Sit</td></tr>
    <tr><td>Lorem Ipsum Dolor Sit</td><td>Lorem Ipsum Dolor Sit</td><td>Lorem Ipsum Dolor Sit</td><td>Lorem Ipsum Dolor Sit</td></tr>
    <tr><td>Lorem Ipsum Dolor Sit</td><td><span class="dash"></span></td><td>Lorem Ipsum Dolor Sit</td><td>Lorem Ipsum Dolor Sit</td></tr>
    <tr><td><span class="dash"></span></td><td>Lorem Ipsum Dolor Sit</td><td>Lorem Ipsum Dolor Sit</td><td><span class="dash"></span></td></tr>
    <tr><td><span class="dash"></span></td><td><span class="dash"></span></td><td><span class="dash"></span></td><td>Lorem Ipsum Dolor Sit</td></tr>
    <tr class="total"><td>15.00$</td><td class="hot">35.00$</td><td>45.00$</td><td class="hot">65.00$</td></tr>
  </table>
  <div class="t web vert" style="left:592px;top:65px">www.company.com</div>
  <div class="brand" style="left:507px;top:304px"><span class="dot"></span>Quillmere</div>
</section>

<section class="slide tree" style="left:656px;top:1514px">
  <svg class="art">
    <defs><radialGradient id="leaf" cx=".5" cy=".45" r=".55"><stop offset="0" stop-color="#e7a07f"/><stop offset=".6" stop-color="#9fb6b4"/><stop offset="1" stop-color="#ffffff"/></radialGradient></defs>
    <rect x="372" y="45" width="240" height="300" rx="40" fill="url(#leaf)" role="img" aria-label="Illustrated tree with orange, teal and green leaves"/>
  </svg>
  <div class="t tag" style="left:483px;top:26px"><b>Quillmere</b> Partnership</div>
  <div class="bar" style="left:252px;top:30px"></div>
  <div class="t section-title" style="left:110px;width:320px;top:40px">TREE <b>INFOGRAPHIC</b></div>
  <div class="item-icon" style="left:33px;top:160px"></div>
  <div class="t item-title" style="left:74px;top:158px">Subtitle Here</div>
  <div class="t item-text" style="left:74px;top:176px">Sed perspiciatis unde omnis iste natus<br>error voluptatem rem.</div>
  <div class="item-icon" style="left:224px;top:162px"></div>
  <div class="t item-title" style="left:265px;top:158px">Subtitle Here</div>
  <div class="t item-text" style="left:265px;top:176px">Sed perspiciatis unde omnis iste<br>natus error voluptatem rem.</div>
  <div class="item-icon hot" style="left:33px;top:234px"></div>
  <div class="t item-title hot" style="left:74px;top:232px">Subtitle Here</div>
  <div class="t item-text" style="left:74px;top:250px">Sed perspiciatis unde omnis iste<br>natus error voluptatem rem.</div>
  <div class="item-icon hot" style="left:224px;top:239px"></div>
  <div class="t item-title hot" style="left:265px;top:237px">Subtitle Here</div>
  <div class="t item-text" style="left:265px;top:255px">Sed perspiciatis unde omnis iste<br>natus error voluptatem rem.</div>
  <div class="t web vert" style="left:592px;top:65px">www.company.com</div>
  <div class="brand" style="left:45px;top:304px"><span class="dot"></span>Quillmere</div>
</section>

<section class="slide planner" style="left:1286px;top:1514px">
  <svg class="art" fill="none" stroke-width="8">
    <g transform="translate(146,137)"><path d="M-38,0 A38,38 0 0 1 38,0" stroke="var(--slate)"/><path d="M38,0 A38,38 0 0 1 -38,0" stroke="#b6bbbd"/><circle cx="-2" cy="-2" r="6" stroke="var(--slate)" stroke-width="2.5"/><line x1="3" y1="3" x2="9" y2="9" stroke="var(--slate)" stroke-width="3"/></g>
    <g transform="translate(229,137)"><path d="M-38,0 A38,38 0 0 1 38,0" stroke="#b6bbbd"/><path d="M38,0 A38,38 0 0 1 -38,0" stroke="var(--orange)"/><rect x="-9" y="-5" width="18" height="12" stroke="var(--orange)" stroke-width="2"/><path d="M-9,-5 L0,3 L9,-5" stroke="var(--orange)" stroke-width="2"/></g>
    <g transform="translate(313,137)"><path d="M-38,0 A38,38 0 0 1 38,0" stroke="var(--slate)"/><path d="M38,0 A38,38 0 0 1 -38,0" stroke="#b6bbbd"/><circle r="6" stroke="var(--slate)" stroke-width="4" stroke-dasharray="3 2"/><circle r="2" fill="var(--slate)" stroke="none"/></g>
    <g transform="translate(397,137)"><path d="M-38,0 A38,38 0 0 1 38,0" stroke="#b6bbbd"/><path d="M38,0 A38,38 0 0 1 -38,0" stroke="var(--orange)"/><path d="M0,11 C-4,4 -7,0 -7,-4 A7,7 0 0 1 7,-4 C7,0 4,4 0,11 Z" fill="var(--orange)" stroke="none"/><circle cy="-4" r="2.5" fill="#fff" stroke="none"/></g>
    <g transform="translate(481,137)"><path d="M-38,0 A38,38 0 0 1 38,0" stroke="var(--slate)"/><path d="M38,0 A38,38 0 0 1 -38,0" stroke="#b6bbbd"/><line x1="-8" y1="-8" x2="8" y2="8" stroke="var(--slate)" stroke-width="3"/><line x1="8" y1="-8" x2="-8" y2="8" stroke="var(--slate)" stroke-width="3"/></g>
  </svg>
  <div class="t tag" style="left:32px;top:26px"><b>Quillmere</b> Partnership</div>
  <div class="bar" style="left:295px;top:36px"></div>
  <div class="t section-title" style="left:0;width:620px;top:48px">BUSINESS <b>PLANNER</b></div>
  <div class="step" style="left:135px;top:207px">1</div>
  <div class="step hot" style="left:218px;top:207px">2</div>
  <div class="step" style="left:302px;top:207px">3</div>
  <div class="step hot" style="left:386px;top:207px">4</div>
  <div class="step" style="left:470px;top:207px">5</div>
  <div class="t step-title" style="left:111px;top:244px">Subtitle Here</div>
  <div class="t step-title" style="left:194px;top:244px">Subtitle Here</div>
  <div class="t step-title" style="left:278px;top:244px">Subtitle Here</div>
  <div class="t step-title" style="left:362px;top:244px">Subtitle Here</div>
  <div class="t step-title" style="left:446px;top:244px">Subtitle Here</div>
  <div class="t step-text" style="left:111px;top:260px">Lorem ipsum dolor sit amet, consectetur</div>
  <div class="t step-text" style="left:194px;top:260px">Lorem ipsum dolor sit amet, consectetur</div>
  <div class="t step-text" style="left:278px;top:260px">Lorem ipsum dolor sit amet, consectetur</div>
  <div class="t step-text" style="left:362px;top:260px">Lorem ipsum dolor sit amet, consectetur</div>
  <div class="t step-text" style="left:446px;top:260px">Lorem ipsum dolor sit amet, consectetur</div>
  <div class="t web vert" style="left:592px;top:65px">www.company.com</div>
  <div class="brand" style="left:507px;top:304px"><span class="dot"></span>Quillmere</div>
</section>

</div>
</body>
</html>
```